Help us redesign PlayHarbor.net ! 550$ of prizes and job position!

Dear Designers,

Playharbor.net is part of a bigger startup which spent the last 5 years doing research & developement.

We built a full software stack for the hosting market, starting from our own virtualization technology to the ecommerce software.
Everything was made either with open source software or with software wrote by us.

We made a HUGE investment to build a great platform which we’re now releasing to the public
Thanks to our flexibility we have an unprecedented number of features that allow us to meet every market demands at an unbelievable price point.

We offer EVERYTHING that a multiplayer server needs in a comprehensive package at a competitive price, without hidden fees or activation costs.

Example of features included for free in each of our products are:

- Preconfigured servers of multiple games;

- Ability to run multiple services and servers at once;

- Voice server;

- Web site with forum and store, ready to be used;

- Databases;

- AntiDDoS Firewall, with hacker protection;

and much much more... Our competition charges extras for such services because they need to license third party software, but we can offer them for free since we built them, and we have full control over the source.

We think we will REVOLUTIONIZE the market, but we also think that our current site design ( http://playharbor.example/ )is not up to the task.

-

We already partnered with an agency to remake the layout of our site, and we picked this layout:

http://tornuvastyles.example/velka/parallax.html

This is a general indication of how we want the layout of the new home page to be.

We will have a first splash screen, to welcome our users, and then a sticky menu to help navigate in a long, parallax home page.

The menu must be on 2 levels, first level to navigate the site, and second level to navigate inside the page.

What we are asking you is to rethink the graphic, to interpret it in a multiplayer way.

You can make as many changes as you want, but we don't want a complete overhaul, rather to adapt the design to our needs.

-

Prizes:

Winner: 300$

2 part time or a full time position as designer for us

Merit prizes: 1x. 20$

Best Creative Design: 55$ of products

Best Colorful Design: 55$ of products

Best Minimal Design: 55$ of products

Most Sales-Driving Design: 55$ of products

Most Inspired Design: 55$ of products

Jury Award: 55$ of products

Worst Design: 15$ of products

Target Market(s)

Our target market are 14-24 years old. 75% are male students. They like videogames and would like to take their passion to the next level.

Industry/Entity Type

Investment

Font styles to use
Sans Serif

Colors

Designer to choose colors to be used in the design.

Requirements
Must have
• It should be a redesign/interpretation of our site in a new theme:

http://playharbor.example/

We want the parallax design and the general layout of the new design.

We want an easy way to integrate streamtube videos in the layout.

You must rethink the graphic to adapt it to our market (multiplayer servers, mostly cubequarry)

We need to explain our products, in a easy and clear way.
Nice to have
• It would be nice to see different types of social content in the page, like friendbook posts, chirpnet feed, streamtube feeds, etc
Should not have
• It should not be too bloated, too flashy, too complicated. The idea is to make it lighter and simpler. These are a nice example of how this type of design can be interpret in a minimal way:

http://www.brevandor.example/
http://honorees.netlaurels.example

Please avoid infringing any copyright.

```html
<!DOCTYPE html>
<html lang="en">
<head>
<meta charset="utf-8">
<title>PlayHarbor</title>
<link rel="stylesheet" href="https://fonts.googleapis.com/css2?family=Bebas+Neue&family=Open+Sans:wght@300;400;600;700&display=swap">
<style>
:root{
  --blue:#2566a8;
  --blue-dark:#1d5590;
  --ink:#4a4a4a;
  --muted:#9a9a9a;
  --dark:#333333;
  --darker:#2b2b2b;
  --light:#f1f1f1;
  --orange:#f7a51c;
  --white:#ffffff;
}
*{margin:0;padding:0;box-sizing:border-box}
html,body{width:1200px;height:2329px;overflow:hidden}
body{position:relative;background:var(--white);font-family:"Open Sans",Arial,sans-serif;color:var(--ink)}
.abs{position:absolute}
.display{font-family:"Bebas Neue",Impact,sans-serif;letter-spacing:1px}

/* hero */
.hero{left:0;top:0;width:1200px;height:546px;overflow:hidden}
.hero-scene{position:absolute;inset:0;background:
  radial-gradient(ellipse 260px 180px at 330px 360px,rgba(160,170,255,.75),transparent 70%),
  radial-gradient(ellipse 300px 200px at 120px 260px,rgba(70,70,80,.8),transparent 70%),
  linear-gradient(180deg,#5d8fb3 0%,#8fb6cf 35%,#a7b8bd 55%,#8c9aa3 75%,#6f7b86 100%)}
.logo{left:511px;top:28px;width:176px;height:176px;border-radius:50%;background:rgba(120,170,210,.45);display:flex;align-items:center;justify-content:center}
.logo-inner{width:152px;height:152px;border-radius:50%;background:#3b4450;display:flex;align-items:center;justify-content:center;color:var(--white);font-weight:600;font-size:23px}
.hero-rule{left:225px;top:274px;width:750px;height:2px;background:var(--blue)}
.hero-title{left:0;top:298px;width:1200px;text-align:center;color:var(--white);font-size:78px;line-height:1}
.hero-text{left:240px;top:399px;width:720px;text-align:center;color:var(--white);font-size:14.5px;line-height:24px}

/* nav */
.nav{left:0;top:546px;width:1200px;height:67px;background:#f4f4f4;border-bottom:3px solid var(--blue);box-shadow:0 14px 24px rgba(0,0,0,.06)}
.nav a{position:absolute;top:20px;transform:translateX(-50%);color:#2a2a2a;text-decoration:none;font-size:25px}
.nav-pointer{left:588px;top:613px;width:0;height:0;border-left:13px solid transparent;border-right:13px solid transparent;border-top:12px solid var(--blue)}

/* services */
.section-title{left:0;width:1200px;text-align:center;color:#3d3d3d;font-size:38px}
.lead{left:225px;width:750px;text-align:center;color:var(--muted);font-size:14.5px;line-height:24px}
.service{top:820px;width:326px;height:340px;text-align:center}
.service + .service{border-left:1px solid #eeeeee}
.service-icon{width:162px;height:162px;border-radius:50%;background:var(--blue);margin:0 auto;display:flex;align-items:center;justify-content:center}
.service h3{margin-top:16px;font-weight:600;font-size:22px;color:#4a4a4a}
.service p{margin:12px auto 0;width:260px;font-size:13px;line-height:18px;color:var(--muted)}
.btn{display:inline-block;background:var(--blue);color:var(--white);font-size:15px;text-decoration:none;padding:5px 11px;border-bottom:2px solid var(--blue-dark)}
.service .btn{margin-top:20px;width:102px}

/* videos */
.videos{left:0;top:1215px;width:1200px;height:517px;background:var(--dark)}
.videos-rule{left:0;top:93px;width:1200px;height:1px;background:#3f3f3f}
.tag{height:48px;background:var(--blue);color:var(--white);font-size:29px;font-weight:300;padding:4px 12px;white-space:nowrap}
.tag b{font-weight:600}
.player{left:110px;top:123px;width:624px;height:354px;background:#000}
.player-art{position:absolute;left:0;top:0;width:624px;height:318px;background:
  radial-gradient(ellipse 140px 110px at 310px 150px,rgba(120,220,200,.8),transparent 70%),
  radial-gradient(ellipse 240px 170px at 150px 120px,rgba(190,60,30,.85),transparent 70%),
  linear-gradient(160deg,#7a2a1a 0%,#c77b2c 40%,#e9c15a 60%,#5d3a28 100%)}
.player-bar{position:absolute;left:0;top:318px;width:624px;height:36px;background:#1b1b1b}
.video-heading{left:765px;top:133px;color:var(--white);font-size:40px;font-weight:400;line-height:50px}
.video-heading b{font-weight:700}
.video-text{left:765px;width:330px;color:#a9a9a9;font-size:13px;line-height:20px}

/* social */
.social-band{left:0;top:1732px;width:1200px;height:50px;background:var(--blue);color:var(--white);font-size:29px;font-weight:300;padding:4px 0 0 121px}
.social-band b{font-weight:600}
.social{left:0;top:1782px;width:1200px;height:179px;background:var(--light)}
.stat{top:0;width:244px;height:179px;border-left:1px solid #e3e3e3;padding:0 0 0 11px}
.stat:first-child{border-left:0}
.stat h4{margin-top:14px;font-weight:400;font-size:20px;color:#555}
.stat .num{position:absolute;top:52px;font-size:45px;font-weight:400;color:#555}
.stat .dot{position:absolute;top:55px;width:58px;height:58px;border-radius:50%;background:var(--blue);border:4px solid #1e5a96}
.stat p{position:absolute;top:128px;width:200px;font-size:13px;line-height:18px;color:#a8a8a8}

/* products */
.products{left:0;top:1961px;width:1200px;height:315px;background:#ececec;border-top:2px solid var(--blue)}
.product-tab{top:82px;height:50px;color:var(--white);font-size:20px;padding:10px 18px}
.product-tab.dark{background:#404040;color:var(--white)}
.product-tab.orange{background:var(--orange);color:#3a3a3a;border-bottom:3px solid #e08d0c}
.plan-list{top:168px;list-style:none}
.plan-list li{position:relative;height:25px;padding-left:28px;font-size:12.5px;color:#555}
.plan-list li::before{content:"";position:absolute;left:0;top:3px;width:11px;height:11px;border-radius:50%;border:1px solid #777;background:var(--white)}
.plan-list li.on::after{content:"";position:absolute;left:3px;top:6px;width:5px;height:5px;border-radius:50%;background:#444}

/* footer */
.footer{left:0;top:2276px;width:1200px;height:53px;background:var(--darker);color:var(--white);font-size:12.5px}
.footer .copy{left:110px;top:17px}
.footer .links{right:110px;top:17px}
</style>
</head>
<body>

<header class="hero abs">
  <div class="hero-scene" role="img" aria-label="Blurred game scene with a battle robot on a beach and blue energy blasts"></div>
  <div class="logo abs"><div class="logo-inner">PlayHarbor</div></div>
  <div class="hero-rule abs"></div>
  <h1 class="hero-title abs display">WELCOME TO PLAY HARBOR</h1>
  <p class="hero-text abs">Lorem ipsum dolor sit amet, consectetur adipisicing elit, sed do eiusmod tempor incididunt ut labore et dolore magna aliqua. Ut enim ad minim veniam, quis nostrud exercitation ullamco laboris nisi ut aliquip ex ea commodo consequat...</p>
</header>

<nav class="nav abs display">
  <a href="#" style="left:335px">HOME</a>
  <a href="#" style="left:449px">CART</a>
  <a href="#" style="left:582px">PRODUCTS</a>
  <a href="#" style="left:733px">SUPPORT</a>
  <a href="#" style="left:863px">LOGIN</a>
</nav>
<div class="nav-pointer abs"></div>

<h2 class="section-title abs display" style="top:648px">OUR FEATURED SERVICES</h2>
<p class="lead abs" style="top:700px">Lorem ipsum dolor sit amet, consectetur adipisicing elit, sed do eiusmod tempor incididunt ut labore et dolore magna aliqua. Ut enim ad minim veniam, quis nostrud exercitation ullamco laboris nisi ut aliquip ex ea commodo consequat...</p>

<div class="service abs" style="left:110px">
  <div class="service-icon">
    <svg width="90" height="90" viewBox="0 0 90 90" fill="none" stroke="#fff" stroke-width="6" stroke-linejoin="round" stroke-linecap="round">
      <path d="M18 60 L52 22 L68 50 Z"/><path d="M28 62 L34 78"/><path d="M62 14 L66 6"/><path d="M72 24 L82 20"/><path d="M74 36 L84 38"/>
    </svg>
  </div>
  <h3>Voice Server</h3>
  <p>Lorem ipsum dolor sit amet, consectetur adipisicing elit, sed do euismod tempor incididunt magna aliqua...</p>
  <a href="#" class="btn">Read More</a>
</div>
<div class="service abs" style="left:436px">
  <div class="service-icon">
    <svg width="100" height="80" viewBox="0 0 100 80" fill="none" stroke="#fff" stroke-width="5" stroke-linejoin="round">
      <rect x="6" y="8" width="88" height="50" rx="3"/>
      <text x="18" y="40" fill="#fff" stroke="none" font-family="Open Sans, sans-serif" font-size="20" font-weight="700">www.|</text>
      <path d="M66 44 L66 74 L74 66 L82 78 L86 76 L78 64 L88 62 Z" fill="#fff" stroke="#2566a8" stroke-width="2"/>
    </svg>
  </div>
  <h3>Voice Server</h3>
  <p>Lorem ipsum dolor sit amet, consectetur adipisicing elit, sed do euismod tempor incididunt magna aliqua...</p>
  <a href="#" class="btn">Read More</a>
</div>
<div class="service abs" style="left:762px">
  <div class="service-icon">
    <svg width="90" height="90" viewBox="0 0 90 90" fill="none" stroke="#fff" stroke-width="6" stroke-linejoin="round" stroke-linecap="round">
      <path d="M12 16 L42 8 L50 10 M12 16 L12 48 C12 66 28 78 42 84 C52 80 62 72 66 62"/>
      <circle cx="64" cy="32" r="17" fill="#fff" stroke="none"/>
      <path d="M56 32 L62 38 L72 26" stroke="#2566a8" stroke-width="5"/>
    </svg>
  </div>
  <h3>Voice Server</h3>
  <p>Lorem ipsum dolor sit amet, consectetur adipisicing elit, sed do euismod tempor incididunt magna aliqua...</p>
  <a href="#" class="btn">Read More</a>
</div>

<section class="videos abs">
  <div class="tag abs" style="left:110px;top:24px">Our Featured <b>Videos!</b></div>
  <div class="videos-rule abs"></div>
  <div class="player abs">
    <div class="player-art" role="img" aria-label="Fantasy game battle artwork with warriors and magic"></div>
    <div class="player-bar">
      <svg width="624" height="36" viewBox="0 0 624 36">
        <rect x="0" y="0" width="624" height="4" fill="#444"/>
        <rect x="0" y="0" width="262" height="4" fill="#c8261e"/>
        <circle cx="262" cy="2" r="6" fill="#ddd"/>
        <rect x="24" y="13" width="3" height="11" fill="#ddd"/><rect x="31" y="13" width="3" height="11" fill="#ddd"/>
        <path d="M66 15 h4 l5 -4 v14 l-5 -4 h-4 z" fill="#ddd"/>
        <rect x="92" y="17" width="42" height="3" fill="#666"/><rect x="92" y="17" width="34" height="3" fill="#c8261e"/><rect x="134" y="13" width="3" height="11" fill="#ddd"/>
        <text x="160" y="23" fill="#999" font-size="10" font-family="Open Sans, sans-serif">04:24 / 09:35</text>
        <text x="558" y="23" fill="#999" font-size="10" font-family="Open Sans, sans-serif">360p</text>
        <path d="M596 12 h5 M596 12 v5 M612 12 h-5 M612 12 v5 M596 26 h5 M596 26 v-5 M612 26 h-5 M612 26 v-5" stroke="#ccc" stroke-width="2"/>
      </svg>
    </div>
  </div>
  <h2 class="video-heading abs">Using A <b>Server</b><br>is <b>Easy!</b></h2>
  <p class="video-text abs" style="top:245px">Lorem ipsum dolor sit amet, consectetur adipisicing elit, sed do eiusmod tempor incididunt ut labore et dolore magna aliqua.</p>
  <p class="video-text abs" style="top:320px">Ut enim ad minim veniam, quis nostrud exercitation ullamco laboris nisi ut aliquip ex ea commodo consequat...</p>
  <a href="#" class="btn abs" style="left:765px;top:409px">Learn More</a>
</section>

<div class="social-band abs">Get <b>Social</b></div>
<section class="social abs">
  <div class="stat abs" style="left:110px"><h4>Rss Subcribers</h4><span class="num" style="left:11px">4451</span><span class="dot" style="left:154px"></span><p style="left:11px">Lorem ipsum dolor sit amet, consectetur adipisicing elit.</p></div>
  <div class="stat abs" style="left:363px"><h4>Friendbook Popularity</h4><span class="num" style="left:11px">10510</span><span class="dot" style="left:153px"></span><p style="left:11px">Lorem ipsum dolor sit amet, consectetur adipisicing elit.</p></div>
  <div class="stat abs" style="left:607px"><h4>People Follow Me</h4><span class="num" style="left:11px">9980</span><span class="dot" style="left:154px"></span><p style="left:11px">Lorem ipsum dolor sit amet, consectetur adipisicing elit.</p></div>
  <div class="stat abs" style="left:852px"><h4>Join Our Group On</h4><span class="num" style="left:11px">1026</span><span class="dot" style="left:153px"></span><p style="left:11px">Lorem ipsum dolor sit amet, consectetur adipisicing elit.</p></div>
</section>

<section class="products abs">
  <div class="tag abs" style="left:110px;top:3px">Our Featured <b>Products</b></div>
  <div class="product-tab dark abs" style="left:110px;width:311px">Total Control Of Your Server</div>
  <div class="product-tab orange abs" style="left:442px;width:311px">DDos Sttack Protection</div>
  <div class="product-tab orange abs" style="left:779px;width:311px">Great Customer Services</div>
  <ul class="plan-list abs" style="left:115px">
    <li>7.0 GB - 39,90€ ~150 slot</li><li class="on">8.0 GB - 44,90€ ~180 slot</li><li>9.0 GB - 49,90€ ~210 slot</li><li>10.0 GB - 54,90€ ~240 slot</li>
  </ul>
  <ul class="plan-list abs" style="left:383px">
    <li>3.0 GB - 19,90€ ~50 slot</li><li>4.0 GB - 24,90€ ~70 slot</li><li>5.0 GB - 29,90€ ~90 slot</li><li>6.0 GB - 34,90€ ~120 slot</li>
  </ul>
  <ul class="plan-list abs" style="left:648px">
    <li>7.0 GB - 39,90€ ~150 slot</li><li>8.0 GB - 44,90€ ~180 slot</li><li>9.0 GB - 49,90€ ~210 slot</li><li>10.0 GB - 54,90€ ~240 slot</li>
  </ul>
  <ul class="plan-list abs" style="left:909px">
    <li>3.0 GB - 19,90€ ~50 slot</li><li>4.0 GB - 24,90€ ~70 slot</li><li>5.0 GB - 29,90€ ~90 slot</li><li>6.0 GB - 34,90€ ~120 slot</li>
  </ul>
</section>

<footer class="footer abs">
  <span class="copy abs">Copyright 2014, Playharbor.com. All Rights Reserved</span>
  <span class="links abs">Terms &amp; Condition &nbsp;|&nbsp; Privacy Policy</span>
</footer>

</body>
</html>
```